Stationary For Harbor Allies
Harbor Allies
Project: Stationary For Harbor Allies
Stationary For Harbor Allies - Consulting
Creative Brief
Professional
Lou Brannick
President
547 Marlow Ln Spring Branch, TX 78070
lbrannick@harborallies4.com
www.harborallies4.com
I will need letterhead and envelopes as well as business cards. Feel free to try different fonts.
quelnor42 quelnor42
Designers, Please focus more on the letterhead and envelopes than the business cards. Thanks!

```html
<!DOCTYPE html>
<html lang="en">
<head>
<meta charset="utf-8">
<title>Harbor Allies – Business Card</title>
<link href="https://fonts.googleapis.com/css2?family=Open+Sans:wght@400;600;700&display=swap" rel="stylesheet">
<style>
  :root {
    --page-bg: #e6e7ea;
    --card-bg: rgba(255, 255, 255, 0.92);
    --card-edge: #d3d7de;
    --navy: #1f3c68;
    --brand-blue: #2a5797;
    --rule-blue: #3b68a8;
    --text-grey: #4d5769;
    --band-grey: #c9ced6;
    --white: #ffffff;
  }
  * { margin: 0; padding: 0; box-sizing: border-box; }
  html, body {
    width: 1200px;
    height: 768px;
    overflow: hidden;
    background: var(--page-bg);
    font-family: "Open Sans", Arial, sans-serif;
  }
  .business-card {
    position: absolute;
    left: 100px;
    top: 94px;
    width: 1000px;
    height: 580px;
    background: var(--card-bg);
    border: 1px solid var(--card-edge);
    border-radius: 6px;
    box-shadow: 0 10px 30px rgba(30, 40, 60, 0.12);
    overflow: hidden;
  }
  .brand {
    position: absolute;
    left: 420px;
    top: 62px;
    display: flex;
    align-items: center;
    gap: 20px;
  }
  .brand-dot {
    width: 74px;
    height: 74px;
    border-radius: 50%;
    background: var(--brand-blue);
  }
  .brand-name {
    font-size: 50px;
    font-weight: 600;
    color: var(--brand-blue);
    letter-spacing: 0.5px;
  }
  .person-name {
    position: absolute;
    left: 60px;
    top: 172px;
    font-size: 44px;
    font-weight: 700;
    color: var(--navy);
  }
  .name-rule {
    position: absolute;
    left: 60px;
    top: 240px;
    width: 880px;
    height: 3px;
    background: var(--rule-blue);
  }
  .person-title {
    position: absolute;
    left: 60px;
    top: 262px;
    font-size: 32px;
    font-weight: 400;
    color: var(--text-grey);
  }
  .contact-list {
    position: absolute;
    right: 60px;
    top: 300px;
    list-style: none;
    text-align: right;
    font-size: 21px;
    line-height: 38px;
    color: var(--text-grey);
  }
  .contact-list li {
    display: flex;
    justify-content: flex-end;
    align-items: center;
    gap: 10px;
  }
  .contact-icon { width: 20px; height: 20px; fill: var(--navy); }
  .contact-icon-line { fill: none; stroke: var(--navy); }
  .icon-spacer { width: 20px; }
  .footer-band {
    position: absolute;
    left: 0;
    bottom: 26px;
    width: 100%;
    height: 46px;
  }
  .footer-band svg { position: absolute; left: 0; top: 0; }
  .footer-url {
    position: absolute;
    left: 40px;
    top: 9px;
    font-size: 20px;
    font-weight: 600;
    color: var(--white);
  }
</style>
</head>
<body>
  <main class="business-card">
    <div class="brand">
      <span class="brand-dot"></span>
      <span class="brand-name">Harbor Allies</span>
    </div>

    <h1 class="person-name">Lou Brannick</h1>
    <div class="name-rule"></div>
    <p class="person-title">President</p>

    <ul class="contact-list">
      <li>547 Marlow Ln<span class="icon-spacer"></span></li>
      <li>Spring Branch, TX 78070<span class="icon-spacer"></span></li>
      <li>012 555 0148
        <svg class="contact-icon" viewBox="0 0 24 24" aria-hidden="true"><path d="M6.6 10.8a15.1 15.1 0 0 0 6.6 6.6l2.2-2.2a1 1 0 0 1 1-.25 11.4 11.4 0 0 0 3.6.57 1 1 0 0 1 1 1V20a1 1 0 0 1-1 1A17 17 0 0 1 3 4a1 1 0 0 1 1-1h3.5a1 1 0 0 1 1 1c0 1.25.2 2.45.57 3.57a1 1 0 0 1-.25 1z"/></svg>
      </li>
      <li>lbrannick@harborallies4.com
        <svg class="contact-icon" viewBox="0 0 24 24" aria-hidden="true"><path d="M3 5h18a1 1 0 0 1 1 1v12a1 1 0 0 1-1 1H3a1 1 0 0 1-1-1V6a1 1 0 0 1 1-1zm0 2v.3l9 5.6 9-5.6V7l-9 5.4z"/></svg>
      </li>
      <li>www.harborallies4.com
        <svg class="contact-icon" viewBox="0 0 24 24" aria-hidden="true"><circle class="contact-icon-line" cx="12" cy="12" r="9" stroke-width="2"/><path class="contact-icon-line" d="M3 12h18M12 3c3 3 3 15 0 18M12 3c-3 3-3 15 0 18" stroke-width="1.6"/></svg>
      </li>
    </ul>

    <div class="footer-band">
      <svg width="1000" height="46" viewBox="0 0 1000 46" aria-hidden="true">
        <rect x="0" y="8" width="1000" height="30" fill="var(--band-grey)"/>
        <path d="M0 0 H300 C335 0 345 46 380 46 H0 Z" fill="var(--navy)"/>
      </svg>
      <span class="footer-url">www.harborallies4.com</span>
    </div>
  </main>
</body>
</html>
```